Bref créative
Bellquist law p.a.
See logo attached
Simple
Hal Bellquist
Board Certified Trial Lawyer
Post Office Box 48716
27 West Caldera Street
Ashmoor Bay, Westmark. 30874
Hal@bellquistlegal.example
Www.halbellquist.example
Here is a version with a slight varation in the size of bellquist law
Here is the final version of the logo with the bellquist law text included with the font that I though was most suitable. There is a white outline on this version that is not on the final version. It is a tif file that will not upload to this server but is on my facebook page. I can email it privately if someone needs it. I think this logo may look better on grey paper. The black background that I have in this attachment may not be feasible since it would require three colors on the letterhead. Anyway, thanks for your help.

```html
<!DOCTYPE html>
<html lang="en">
<head>
<meta charset="utf-8">
<title>Bellquist Law P.A. — Stationery</title>
<link rel="stylesheet" href="https://fonts.googleapis.com/css2?family=Cormorant+Garamond:wght@600&family=Open+Sans:wght@400&display=swap">
<style>
  :root {
    --bg: #e6e6e6;
    --paper: #ffffff;
    --ink: #3a3a3a;
    --muted: #6b6b6b;
    --accent: #f26522;
    --card-dark: #111111;
    --card-url: #bdbdbd;
    --window: #eeeeee;
    --flap: #f4f4f4;
    --edge: #d4d4d4;
  }
  * { box-sizing: border-box; margin: 0; padding: 0; }
  html, body { width: 1200px; height: 847px; overflow: hidden; background: var(--bg); }
  .canvas { position: relative; width: 1200px; height: 847px; }

  .brand { display: flex; align-items: center; gap: 6px; }
  .brand-mark { width: 10px; height: 10px; background: var(--accent); flex: none; }
  .brand-name {
    font-family: "Cormorant Garamond", serif; font-weight: 600;
    color: var(--accent); text-transform: uppercase; letter-spacing: 0.08em; white-space: nowrap;
  }
  .small { font-family: "Open Sans", sans-serif; font-weight: 400; color: var(--ink); white-space: nowrap; }

  /* Letterhead */
  .letterhead {
    position: absolute; left: 432px; top: 19px; width: 348px; height: 809px;
    background: var(--paper); border: 1px solid var(--edge);
  }
  .letterhead .brand { position: absolute; left: 0; right: 0; top: 56px; justify-content: center; }
  .letterhead .brand-name { font-size: 15px; }
  .letterhead-footer {
    position: absolute; left: 0; right: 0; bottom: 14px; text-align: center;
    font-size: 6.5px; line-height: 1.6;
  }

  /* Envelope */
  .envelope {
    position: absolute; left: 72px; top: 324px; width: 612px; height: 324px;
    background: var(--paper); border: 1px solid var(--edge);
  }
  .envelope-flap { position: absolute; left: 0; top: 0; width: 100%; height: 120px; }
  .flap-url {
    position: absolute; left: 0; right: 0; top: 40px; text-align: center;
    font-size: 8px; letter-spacing: 0.12em; transform: rotate(180deg); color: var(--muted);
  }
  .envelope .brand { position: absolute; left: 30px; top: 150px; }
  .envelope .brand-name { font-size: 13px; }
  .envelope-window {
    position: absolute; left: 30px; top: 210px; width: 236px; height: 68px;
    background: var(--window); border: 1px solid var(--edge); border-radius: 6px;
  }
  .envelope-address { position: absolute; left: 30px; bottom: 14px; font-size: 7px; }

  /* Business cards */
  .card { position: absolute; left: 828px; width: 336px; height: 162px; border: 1px solid var(--edge); }
  .card-front { top: 355px; background: var(--card-dark); border-color: var(--card-dark); }
  .card-front .brand { position: absolute; left: 56px; top: 62px; }
  .card-front .brand-name { font-size: 16px; }
  .card-front .card-url {
    position: absolute; left: 74px; top: 92px; font-size: 8px; color: var(--card-url); letter-spacing: 0.06em;
  }
  .card-back { top: 547px; height: 173px; background: var(--paper); }
  .card-holder { position: absolute; left: 18px; top: 18px; }
  .holder-name { font-size: 11px; }
  .holder-title { font-size: 6.5px; color: var(--muted); margin-top: 2px; }
  .card-back .brand { position: absolute; right: 22px; top: 74px; }
  .card-back .brand-name { font-size: 11px; }
  .card-contact { position: absolute; left: 18px; top: 98px; font-size: 6.5px; line-height: 1.55; }
</style>
</head>
<body>
<main class="canvas">

  <section class="letterhead">
    <div class="brand"><span class="brand-mark"></span><span class="brand-name">Bellquist Law P.A.</span></div>
    <footer class="letterhead-footer small">
      Post Office Box 48716 | 27 West Caldera Street | Ashmoor Bay, Westmark. 30874<br>
      P: 555.201.0142 C: 555.201.0187 F: 555.201.0163 | Hal@bellquistlegal.example | Www.halbellquist.example
    </footer>
  </section>

  <section class="envelope">
    <svg class="envelope-flap" viewBox="0 0 612 120" preserveAspectRatio="none" aria-hidden="true">
      <path d="M0 0 H612 V6 L330 112 Q306 120 282 112 L0 6 Z" fill="#f4f4f4" stroke="#d4d4d4" stroke-width="1"/>
    </svg>
    <div class="flap-url small">Www.halbellquist.example</div>
    <div class="brand"><span class="brand-mark"></span><span class="brand-name">Bellquist Law P.A.</span></div>
    <div class="envelope-window"></div>
    <div class="envelope-address small">Post Office Box 48716 | 27 West Caldera Street | Ashmoor Bay, Westmark. 30874</div>
  </section>

  <section class="card card-front">
    <div class="brand"><span class="brand-mark"></span><span class="brand-name">Bellquist Law P.A.</span></div>
    <div class="card-url small">Www.halbellquist.example</div>
  </section>

  <section class="card card-back">
    <div class="card-holder small">
      <div class="holder-name">Hal Bellquist</div>
      <div class="holder-title">Board Certified Trial Lawyer</div>
    </div>
    <div class="brand"><span class="brand-mark"></span><span class="brand-name">Bellquist Law P.A.</span></div>
    <div class="card-contact small">
      Post Office Box 48716<br>
      27 West Caldera Street<br>
      Ashmoor Bay, Westmark. 30874<br>
      P: 555.201.0142 C: 555.201.0187 F: 555.201.0163 | Hal@bellquistlegal.example
    </div>
  </section>

</main>
</body>
</html>
```